Business Card Design for a Technology Development Company

******* PLEASE NOTE (ALL DESIGNERS): I am going to finish the competition on Monday the 9th July (NOT SATURDAY 15TH). I have some designs I like and need to get them printed next week. Please submit any designs today or tomorrow. *******

PLEASE READ ALL OF THE REQUIREMENTS!!! I've rejected lot's of designs in the past because they didn't read the basic requirements - thanks and good luck!

Quill Harbor is a UK technology / small holding company that invests in startups and develops new ideas. In addition it provides IT Professional Services.

Ideally the design will be simple, professional, smart, and sophisticated, and overall be nice to look at. You can be creative as you like with the design, equally as simple as you like - you guys are the professionals so I'll leave it to your inspiration (make sure you incorporate the logo)!
Updates

PLEASE NOTE (ALL DESIGNERS): I am going to finish the competition on Monday the 9th July (NOT SATURDAY 15TH).  I have some designs I like and need to get them printed next week.  Please submit any designs today or tomorrow.

Target Market(s)

Enterprises / corporations / public sector / technical engineers / investors. More www.brantelix.com / www.vornel.com than www.pibbleroo.com!

Industry/Entity Type

Business

Requirements
Must have
• It should be modern and any artwork (if used) should be simple
- Pastel colours, dark and light colours, and shades are preferred over bright colours
- The design should incorporate the attached Quill Harbor logo and the logo colour scheme
- The logo should be on both sides. The back should just have the logo, maybe with some additional graphics
- It must have the following information on:

FirstName SecondName
Company Position
Email: name@quillharbor.co.uk
Mobile: +44 (0) 7700 984312

- The final design should be for a UK business card, dimensions: 85mm × 55mm
- The final design should have bleed marks to allow for printing and should be given in vector formats (EPS and AI)
Nice to have
• The Logo can be separated from the font in the logo on the front of the card. This isn't necessary or required, just to know it's not a limitation.
Should not have
• No bright colours (I prefer pastel colours, dark and light colours, and shades)
- Fonts that are to thin
- Effects or designs that make it difficult to print
- Italic or old fashioned looking fonts, i.e. anything like Times New Roman is a NO!

```html
<!DOCTYPE html>
<html lang="en">
<head>
<meta charset="utf-8">
<title>Quill Harbor — Business Card</title>
<link href="https://fonts.googleapis.com/css2?family=Architects+Daughter&family=Montserrat:wght@600&display=swap" rel="stylesheet">
<style>
  :root {
    --backdrop: #434041;
    --card-black: #0a090a;
    --teal: #4fa9b6;
    --teal-deep: #1d6d7a;
    --ink-light: #f4f4f4;
  }
  html, body {
    margin: 0;
    padding: 0;
    width: 927px;
    height: 1200px;
    overflow: hidden;
    background: var(--backdrop);
  }
  .canvas {
    position: relative;
    width: 927px;
    height: 1200px;
    background: var(--backdrop);
  }
  .card-back {
    position: absolute;
    left: 57px;
    top: 0;
    width: 814px;
    height: 600px;
    background: var(--card-black);
  }
  .brand {
    position: absolute;
    display: flex;
    align-items: center;
    gap: 26px;
    font-family: "Montserrat", sans-serif;
    font-weight: 600;
    color: var(--teal);
    white-space: nowrap;
  }
  .brand-dot {
    display: block;
    border-radius: 50%;
    background: var(--teal);
    flex: none;
  }
  .card-back .brand {
    left: 118px;
    top: 245px;
    font-size: 56px;
  }
  .card-back .brand-dot {
    width: 84px;
    height: 84px;
  }
  .front-strip {
    position: absolute;
    left: 0;
    top: 600px;
    width: 218px;
    height: 600px;
    background: var(--card-black);
  }
  .front-strip .strip-dot {
    position: absolute;
    left: 66px;
    top: 30px;
    width: 84px;
    height: 84px;
    border-radius: 50%;
    background: var(--teal);
  }
  .front-strip .strip-name {
    position: absolute;
    left: 80px;
    top: 148px;
    writing-mode: vertical-rl;
    font-family: "Montserrat", sans-serif;
    font-weight: 600;
    font-size: 48px;
    color: var(--teal);
    white-space: nowrap;
  }
  .front-decor {
    position: absolute;
    left: 748px;
    top: 630px;
    width: 150px;
    height: 150px;
    border-radius: 50%;
    background: var(--teal-deep);
    opacity: 0.55;
  }
  .front-details {
    position: absolute;
    left: 218px;
    top: 600px;
    width: 709px;
    height: 600px;
    font-family: "Architects Daughter", cursive;
    color: var(--ink-light);
    text-align: center;
  }
  .person-name {
    position: absolute;
    left: 0;
    width: 612px;
    top: 230px;
    margin: 0;
    font-size: 46px;
    font-weight: 400;
    letter-spacing: 1px;
  }
  .person-role {
    position: absolute;
    left: 0;
    width: 612px;
    top: 298px;
    margin: 0;
    font-size: 37px;
    letter-spacing: 1px;
  }
  .contact {
    position: absolute;
    left: 0;
    width: 680px;
    top: 438px;
    margin: 0;
    font-size: 39px;
    line-height: 56px;
    letter-spacing: 1px;
  }
</style>
</head>
<body>
  <div class="canvas">
    <section class="card-back">
      <div class="brand">
        <span class="brand-dot"></span>
        <span class="brand-name">Quill Harbor</span>
      </div>
    </section>

    <aside class="front-strip">
      <span class="strip-dot"></span>
      <span class="strip-name">Quill Harbor</span>
    </aside>

    <div class="front-decor"></div>

    <section class="front-details">
      <h1 class="person-name">firstname secondname</h1>
      <p class="person-role">company position</p>
      <p class="contact">
        email: name@quillharbor.co.uk<br>
        mobile: +44 (0) 7700 984312
      </p>
    </section>
  </div>
</body>
</html>
```